BRISK GUARD WEBSITE BANNER DESIGN OF AWESOME

Please take a look at the attached Banner. I want a redesign Idea. The requirements are below.

1)Must Use Website Background
2)Must Use Photo Provided
3)Must Include Button
4)Website the banner will be used on you can see the current at the bottom of the page: https://b.plomvarn.com

Target Market(s)

Anyone Seeking Security Guard Services

```html
<!DOCTYPE html>
<html lang="en">
<head>
<meta charset="utf-8">
<title>Brisk Guard — Website Banner</title>
<link rel="stylesheet" href="https://fonts.googleapis.com/css2?family=Montserrat:wght@500;600;700;800&display=swap">
<style>
  :root {
    --page-bg: #f1f2f4;
    --navy-deep: #0d1b33;
    --navy: #16294a;
    --blue: #1f4274;
    --blue-light: #2f62a3;
    --accent: #f6a81c;
    --accent-dark: #e08e0b;
    --white: #ffffff;
    --muted: #b9c6da;
    --photo-dark: #0b1424;
    --photo-mid: #24344e;
  }
  * { box-sizing: border-box; margin: 0; padding: 0; }
  html, body { width: 870px; height: 1200px; overflow: hidden; }
  body {
    background: var(--page-bg);
    font-family: "Montserrat", Arial, sans-serif;
    color: var(--white);
    position: relative;
  }

  /* ---------- website page ---------- */
  .site {
    position: absolute; left: 35px; top: 90px; width: 800px;
    box-shadow: 0 6px 24px rgba(13, 27, 51, .18);
  }
  .site-header {
    height: 44px; background: var(--navy-deep);
    display: flex; align-items: center; padding: 0 22px;
  }
  .brand { display: flex; align-items: center; gap: 6px; font-weight: 800; font-size: 11px; letter-spacing: .5px; color: var(--white); }
  .brand-mark { width: 14px; height: 14px; background: var(--accent); border-radius: 50%; }
  .nav { margin-left: auto; display: flex; align-items: center; gap: 16px; font-size: 8px; font-weight: 600; letter-spacing: .4px; color: var(--muted); }
  .nav .active { color: var(--white); }
  .nav-cta { background: var(--accent); color: var(--navy-deep); padding: 6px 10px; border-radius: 3px; font-weight: 700; }

  .site-footer { background: var(--navy); padding: 22px 40px 18px; display: flex; justify-content: space-between; }
  .contact-col { display: flex; flex-direction: column; gap: 10px; font-size: 9px; color: var(--muted); }
  .contact-line { display: flex; align-items: center; gap: 8px; }
  .contact-line svg { width: 12px; height: 12px; flex: none; }
  .copyright { background: var(--navy-deep); height: 26px; display: flex; align-items: center; justify-content: center; font-size: 7.5px; color: var(--muted); }

  /* ---------- banner ---------- */
  .banner {
    position: relative; width: 800px; height: 280px; overflow: hidden;
    background: linear-gradient(100deg, var(--navy) 0%, var(--blue) 45%, var(--blue-light) 100%);
  }
  .banner.standalone { position: absolute; left: 35px; top: 650px; box-shadow: 0 6px 24px rgba(13, 27, 51, .18); }
  .banner-sheen {
    position: absolute; inset: 0;
    background: linear-gradient(115deg, transparent 30%, rgba(255,255,255,.07) 42%, transparent 55%);
  }
  .guard-photo {
    position: absolute; top: 0; right: 0; width: 380px; height: 280px;
    clip-path: polygon(30% 0, 100% 0, 100% 100%, 0 100%);
    background:
      radial-gradient(ellipse 45% 35% at 70% 38%, rgba(214,226,245,.55), transparent 70%),
      linear-gradient(160deg, var(--photo-mid) 0%, var(--photo-dark) 75%);
  }
  .accent-stripes { position: absolute; inset: 0; width: 800px; height: 280px; }
  .badge {
    position: absolute; top: 22px; right: 28px;
    display: flex; align-items: center; gap: 6px;
    font-weight: 800; font-size: 13px; color: var(--white); letter-spacing: .5px;
  }
  .badge-square { width: 14px; height: 14px; background: var(--accent); }

  .banner-copy { position: absolute; left: 42px; top: 46px; }
  .headline { font-size: 38px; font-weight: 800; line-height: 1.05; letter-spacing: -.3px; }
  .headline em { font-style: normal; color: var(--accent); }
  .tagline { font-size: 15px; font-weight: 500; margin-top: 6px; }
  .features { display: flex; gap: 26px; margin-top: 28px; }
  .feature { display: flex; align-items: flex-start; gap: 8px; font-size: 14px; font-weight: 700; line-height: 1.15; }
  .feature svg { width: 16px; height: 16px; flex: none; margin-top: 1px; }
  .cta {
    display: inline-block; margin-top: 30px;
    background: var(--accent); color: var(--navy-deep);
    font-size: 11px; font-weight: 800; letter-spacing: .6px;
    padding: 10px 20px; border-radius: 16px;
    box-shadow: 0 3px 0 var(--accent-dark);
  }
</style>
</head>
<body>

<svg width="0" height="0" style="position:absolute" aria-hidden="true">
  <defs>
    <symbol id="icon-tick" viewBox="0 0 16 16">
      <rect x="1" y="1" width="14" height="14" rx="2" fill="none" stroke="#f6a81c" stroke-width="1.6"/>
      <path d="M4 8.3l2.7 2.7L12 5.3" fill="none" stroke="#f6a81c" stroke-width="2" stroke-linecap="round" stroke-linejoin="round"/>
    </symbol>
    <symbol id="icon-pin" viewBox="0 0 12 12">
      <path d="M6 11s4-4.2 4-6.5A4 4 0 0 0 2 4.5C2 6.8 6 11 6 11z" fill="#f6a81c"/>
      <circle cx="6" cy="4.6" r="1.4" fill="#16294a"/>
    </symbol>
    <symbol id="icon-phone" viewBox="0 0 12 12">
      <path d="M3 1.2l1.8 2.3-1 1.2a6.5 6.5 0 0 0 3.5 3.5l1.2-1 2.3 1.8-.9 1.6C5.6 10.5 1.5 6.4 1.4 2.1z" fill="#f6a81c"/>
    </symbol>
    <symbol id="icon-mail" viewBox="0 0 12 12">
      <rect x="1" y="2.5" width="10" height="7" rx="1" fill="#f6a81c"/>
      <path d="M1.5 3.2L6 6.5l4.5-3.3" fill="none" stroke="#16294a" stroke-width="1"/>
    </symbol>
    <symbol id="icon-clock" viewBox="0 0 12 12">
      <circle cx="6" cy="6" r="5" fill="#f6a81c"/>
      <path d="M6 3.2V6l2 1.3" fill="none" stroke="#16294a" stroke-width="1.1" stroke-linecap="round"/>
    </symbol>
  </defs>
</svg>

<main class="site">
  <header class="site-header">
    <div class="brand"><span class="brand-mark"></span>BRISK GUARD</div>
    <nav class="nav">
      <span class="active">HOME</span>
      <span>ABOUT US</span>
      <span>SERVICES</span>
      <span>CAREERS</span>
      <span>CONTACT US</span>
      <span>CLIENT LOGIN</span>
      <span class="nav-cta">REQUEST QUOTE</span>
    </nav>
  </header>

  <section class="banner">
    <div class="banner-sheen"></div>
    <div class="guard-photo" role="img" aria-label="Security guard in a dark uniform shining a flashlight up a stairway"></div>
    <svg class="accent-stripes" viewBox="0 0 800 280" aria-hidden="true">
      <polygon points="510,0 538,0 500,70 472,70" fill="#f6a81c"/>
      <polygon points="546,0 558,0 520,70 508,70" fill="#f6a81c" opacity=".8"/>
      <polygon points="760,200 800,200 800,280 716,280" fill="#f6a81c"/>
      <polygon points="736,210 748,210 706,280 694,280" fill="#f6a81c" opacity=".8"/>
    </svg>
    <div class="badge"><span class="badge-square"></span>BRISK GUARD</div>
    <div class="banner-copy">
      <h1 class="headline">Get Secured <em>TODAY</em></h1>
      <p class="tagline">We take your security personal.</p>
      <ul class="features">
        <li class="feature"><svg><use href="#icon-tick"/></svg><span>Client<br>Portal</span></li>
        <li class="feature"><svg><use href="#icon-tick"/></svg><span>24x7<br>Dispatch</span></li>
        <li class="feature"><svg><use href="#icon-tick"/></svg><span>No Binding<br>Contracts</span></li>
      </ul>
      <span class="cta">GET STARTED</span>
    </div>
  </section>

  <footer class="site-footer">
    <div class="contact-col">
      <div class="contact-line"><svg><use href="#icon-pin"/></svg>12 Harbor Lane, Suite 4</div>
      <div class="contact-line"><svg><use href="#icon-phone"/></svg>(555) 010-2847</div>
    </div>
    <div class="contact-col">
      <div class="contact-line"><svg><use href="#icon-mail"/></svg>hello@plomvarn.com</div>
      <div class="contact-line"><svg><use href="#icon-phone"/></svg>(555) 010-3391</div>
    </div>
    <div class="contact-col">
      <div class="contact-line"><svg><use href="#icon-clock"/></svg>Open 24 Hours</div>
      <div class="contact-line"><svg><use href="#icon-phone"/></svg>(555) 010-5520</div>
    </div>
  </footer>
  <div class="copyright">© 2024 Brisk Guard. All rights reserved.</div>
</main>

<section class="banner standalone">
  <div class="banner-sheen"></div>
  <div class="guard-photo" role="img" aria-label="Security guard in a dark uniform shining a flashlight up a stairway"></div>
  <svg class="accent-stripes" viewBox="0 0 800 280" aria-hidden="true">
    <polygon points="510,0 538,0 500,70 472,70" fill="#f6a81c"/>
    <polygon points="546,0 558,0 520,70 508,70" fill="#f6a81c" opacity=".8"/>
    <polygon points="760,200 800,200 800,280 716,280" fill="#f6a81c"/>
    <polygon points="736,210 748,210 706,280 694,280" fill="#f6a81c" opacity=".8"/>
  </svg>
  <div class="badge"><span class="badge-square"></span>BRISK GUARD</div>
  <div class="banner-copy">
    <h2 class="headline">Get Secured <em>TODAY</em></h2>
    <p class="tagline">We take your security personal.</p>
    <ul class="features">
      <li class="feature"><svg><use href="#icon-tick"/></svg><span>Client<br>Portal</span></li>
      <li class="feature"><svg><use href="#icon-tick"/></svg><span>24x7<br>Dispatch</span></li>
      <li class="feature"><svg><use href="#icon-tick"/></svg><span>No Binding<br>Contracts</span></li>
    </ul>
    <span class="cta">GET STARTED</span>
  </div>
</section>

</body>
</html>
```